Visitenkarten-Design für Ferienhausvermietung
Zielgruppe
Vermietung eines Ferienhauses
Aufgabenstellung
Die Visitenkarte sollte edel und hochwertig wirken...
Es wäre mir wichtig, dass die Visitenkarte im Querformat erstellt wird.
Die Farben vom Logo lauten:
green: C = 43 M = 0 Y = 100 N = 16
brown: C = 39 M = 57 J = 87 N = 53
sky blue: C = 14 M = 6 J = 6 N = 0
Aber bitte nicht so viel in den Visitenkarten verwenden. Die Visitenkarten sollen eher neutral gehalten werden.
Die Schriften
font
Lindeneck : Satisfaction
Ferienhaus : Corbert Regular
Flyer-Design für Ferienhausvermietung Flyer-Design für Ferienhausvermietung"
Es soll ein Flyer im Format DIN A4 erstellt werden. Der beidseitig bedruckt wird und dann 6seitig gefaltet wird. Ich benötige für den Flyer: Beschreibung/Ausstattung des Ferienhauses Beschreibung der Lage Beschreibung der Umgebung Anfahrt/Lage/Kontakt
Logo-Design für Ferienhaus ´Sa Morta´auf Mallorca mit eigenem Tennisplatz und Pool Logo-Design für Ferienhaus ´Sa Morta´auf Mallorca mit eigenem Tennisplatz und Pool"
Sie können sich meine Finca auf der Website: Casitorvent anschauen. Ort: Costitx Name des Hauses: Finca Reblat (heißt nur auf der Website so). Der Name am Tor Haus: Finca Sa Morta. Ich mag es gerne klassisch
Logo-Design für ein Feriendorf an der Ostsee Logo-Design für ein Feriendorf an der Ostsee"
* Nicht zu bunt, nicht zu verspielt, möglichst klar und aufgeräumt * In 2D, keine Schattierungen, keine Fotos im Hintergrund o. ä.. * Das Logo muss in allen Medien gut darstellbar sein! * Es sollte modern wirken, dennoch fröhlich, warm und einladend * Der Strand-/Wasserbezug muss deutlich we..
Flyer-Design für Ferienhaus Flyer-Design für Ferienhaus"
Flyerdesign für Ferienhaus: Din-Lang 2x gefalzt (übliche Format), 3 Seiten vorne und hinten.  Es sollte nach Möglichkeit an unsere Webseite (www.ferienhaus-kormoran-tidewik.de) angepasst werden, druckfertig sein und per PDF auf unserer Webseite zum Downloaden integriert werden können. Meh..
Logo-Design für Ferienhaus Logo-Design für Ferienhaus"
Wir suchen ein Moderenes Design gern berücksichtig in Kombination mit dem Naturpark Velmtaler Höhen. Da das Ferienhaus sich dort befindet.

```html
<!DOCTYPE html>
<html lang="de">
<head>
<meta charset="utf-8">
<title>Ferienhaus Lindeneck – Visitenkarte</title>
<link rel="stylesheet" href="https://fonts.googleapis.com/css2?family=Quicksand:wght@400&display=swap">
<style>
  :root {
    --canvas-bg: #ececec;
    --card-bg: #ffffff;
    --brown: #5b3f1f;
    --green: #7aab1e;
    --sky: #d4dfe3;
  }
  * { margin: 0; padding: 0; box-sizing: border-box; }
  html, body {
    width: 1037px;
    height: 1200px;
    overflow: hidden;
    background: var(--canvas-bg);
  }
  .sheet {
    width: 1037px;
    height: 1200px;
    display: flex;
    flex-direction: column;
    align-items: center;
    justify-content: center;
    gap: 76px;
  }
  .card {
    width: 760px;
    height: 492px;
    background: var(--card-bg);
    box-shadow: 0 2px 4px rgba(0,0,0,0.08), 0 10px 28px rgba(0,0,0,0.08);
    display: flex;
    align-items: center;
    justify-content: center;
    font-family: "Quicksand", sans-serif;
    font-weight: 400;
  }
  .brand {
    display: flex;
    align-items: center;
    gap: 18px;
    color: var(--brown);
    font-size: 46px;
    letter-spacing: 0.02em;
  }
  .brand-dot {
    width: 30px;
    height: 30px;
    border-radius: 50%;
    background: var(--sky);
    border: 3px solid var(--brown);
  }
  .contact {
    text-align: center;
    font-size: 20px;
    line-height: 1.35;
  }
  .contact-address { color: var(--brown); }
  .contact-online {
    color: var(--green);
    margin-top: 64px;
  }
</style>
</head>
<body>
  <main class="sheet">
    <section class="card card-front" aria-label="Vorderseite">
      <div class="brand">
        <span class="brand-dot"></span>
        <span class="brand-name">Lindeneck</span>
      </div>
    </section>

    <section class="card card-back" aria-label="Rückseite">
      <div class="contact">
        <p class="contact-address">
          Ferienhaus Lindeneck<br>
          Ahornweg 12<br>
          97820 Talbrunn<br>
          info@lindeneck-ferienhaus.de
        </p>
        <p class="contact-online">
          Tel: 09871 / 55 20 418<br>
          www.lindeneck-ferienhaus.de
        </p>
      </div>
    </section>
  </main>
</body>
</html>
```